Design a book cover for a presidential candidate

Design a print and e-book cover from the attached materials. We want a patriotic nonpartisan cover for an independent candidate in the 2016 Presidential race. The design should be somewhat futuristic, technologically advanced, and yet communicate fairness and balance. The Title, subtitles, back cover copy and quotes are all in the attached material. Use any of the photos attached.

```html
<!DOCTYPE html>
<html lang="en">
<head>
<meta charset="utf-8">
<title>A Citizen for Everyone — Book Cover</title>
<link href="https://fonts.googleapis.com/css2?family=Tinos:ital,wght@0,700;1,700&family=Arimo:wght@700&display=swap" rel="stylesheet">
<style>
  :root {
    --cover-bg: #3a3a3c;
    --gold: #c9a379;
    --photo-dark: #2c2c2c;
    --photo-mid: #7a7a78;
    --photo-light: #b5b5b2;
  }
  html, body {
    margin: 0;
    padding: 0;
    width: 1200px;
    height: 886px;
    overflow: hidden;
    background: var(--cover-bg);
  }
  .cover {
    position: relative;
    width: 1200px;
    height: 886px;
    background: var(--cover-bg);
    color: var(--gold);
    font-family: "Tinos", "Times New Roman", serif;
  }
  .back-author {
    position: absolute;
    left: 0;
    width: 570px;
    top: 74px;
    margin: 0;
    text-align: center;
    font-style: italic;
    font-weight: 700;
    font-size: 48px;
    line-height: 1;
  }
  .back-blurb {
    position: absolute;
    left: 0;
    width: 554px;
    top: 166px;
    margin: 0;
    text-align: center;
    font-style: italic;
    font-weight: 700;
    font-size: 18px;
    line-height: 29px;
  }
  .back-website {
    position: absolute;
    left: 0;
    width: 556px;
    top: 838px;
    margin: 0;
    text-align: center;
    font-style: italic;
    font-weight: 700;
    font-size: 22px;
    line-height: 1;
  }
  .spine-text {
    position: absolute;
    left: 579px;
    margin: 0;
    font-family: "Arimo", "Verdana", sans-serif;
    font-weight: 700;
    font-size: 28px;
    letter-spacing: 2.4px;
    white-space: nowrap;
    transform-origin: 0 0;
    transform: rotate(90deg) translateY(-50%);
    line-height: 1;
  }
  .spine-title { top: 30px; }
  .spine-author { top: 660px; letter-spacing: 1.6px; }
  .front-title {
    position: absolute;
    left: 600px;
    width: 600px;
    top: 40px;
    margin: 0;
    text-align: center;
    font-style: italic;
    font-weight: 700;
    font-size: 55px;
    line-height: 84px;
    letter-spacing: 1px;
  }
  .front-subtitle {
    position: absolute;
    left: 600px;
    width: 600px;
    top: 200px;
    margin: 0;
    text-align: center;
    font-weight: 700;
    font-size: 36px;
    line-height: 44px;
  }
  .author-photo {
    position: absolute;
    left: 600px;
    top: 262px;
    width: 600px;
    height: 450px;
    display: block;
  }
  .front-author {
    position: absolute;
    right: 34px;
    top: 734px;
    margin: 0;
    font-style: italic;
    font-weight: 700;
    font-size: 48px;
    line-height: 1;
  }
  .front-tagline {
    position: absolute;
    left: 650px;
    width: 510px;
    top: 790px;
    margin: 0;
    text-align: center;
    font-style: italic;
    font-weight: 700;
    font-size: 22px;
    line-height: 38px;
  }
</style>
</head>
<body>
<main class="cover">
  <section class="back-cover">
    <h2 class="back-author">Dale Harmon</h2>
    <p class="back-blurb">Dale Harmon is an independent candidate in the<br>
      2016 Presidential race whose ideas speak to voters<br>
      on the right and the left. His plans aim to modernize how<br>
      the country pays its bills. Harmon proposes a simpler tax code,<br>
      a budget that balances through transparent public accounting,<br>
      retiring federal debt on a steady decade-long schedule,<br>
      and launching a Public Lending Network designed to<br>
      lower the price of home loans and college tuition for families.</p>
    <p class="back-website">www.daleharmon2016.com</p>
  </section>

  <section class="spine">
    <p class="spine-text spine-title">A CITIZEN FOR EVERYONE</p>
    <p class="spine-text spine-author">Dale Harmon</p>
  </section>

  <section class="front-cover">
    <h1 class="front-title">A CITIZEN FOR<br>EVERYONE</h1>
    <p class="front-subtitle">My blueprint for a fair nation</p>
    <svg class="author-photo" role="img" aria-label="Black and white portrait of the candidate in a leather jacket with a wooded mountain hillside behind him" viewBox="0 0 600 450" preserveAspectRatio="none">
      <defs>
        <linearGradient id="photoTone" x1="0" y1="0" x2="1" y2="1">
          <stop offset="0" stop-color="var(--photo-mid)"/>
          <stop offset="0.45" stop-color="var(--photo-light)"/>
          <stop offset="1" stop-color="var(--photo-dark)"/>
        </linearGradient>
      </defs>
      <rect width="600" height="450" fill="url(#photoTone)"/>
    </svg>
    <h2 class="front-author">Dale Harmon</h2>
    <p class="front-tagline">A Declaration of Balance<br>For the Shared Prosperity of All</p>
  </section>
</main>
</body>
</html>
```